Redesign CanvoMira's Artist Profile Page

CanvoMira is a contemporary arts website that has a large worldwide community of artists with profile pages for each artist showing artwork, exhibits, bio data, etc.

For an example please see: http://www.canvomira-example.com/global/artists/show/40731-orin-haskel

We would like a slight redesign on these pages within the context of the current website. We are interested in modernizing and lightening the design. The artwork should be the primary focus.

Target Market(s)

Professional artists, galleries and collectors

Industry/Entity Type

Artists

Requirements
Must have
• All the current functionality on the page.

```html
<!DOCTYPE html>
<html lang="en">
<head>
<meta charset="utf-8">
<title>Orin Haskel – CanvoMira Worldwide</title>
<link href="https://fonts.googleapis.com/css2?family=Ubuntu:wght@400;500;700&family=Arimo:wght@400;700&display=swap" rel="stylesheet">
<style>
:root{
  --page:#f3f3f3;
  --bar:#2f2f2f;
  --accent:#c3c822;
  --accent-text:#a9ad1c;
  --ink:#3d3d3d;
  --ink-soft:#555;
  --line:#d9d9d9;
  --panel:#fff;
  --box:#f5f5f5;
}
*{box-sizing:border-box;margin:0;padding:0}
html,body{width:874px;height:1200px;overflow:hidden;background:var(--page)}
body{position:relative;font-family:"Ubuntu",sans-serif;color:var(--ink)}
.abs{position:absolute}
.citybar{left:0;top:0;width:874px;height:29px;background:var(--bar);color:var(--accent);font-size:11px;display:flex;align-items:center;justify-content:center;gap:4px;box-shadow:0 2px 3px rgba(0,0,0,.3)}
.citybar .sep{color:#999}
.brand{left:92px;top:48px;display:flex;align-items:baseline;gap:6px}
.brand-name{font-size:40px;font-weight:500;color:#555;letter-spacing:-2px}
.brand-sub{font-size:17px;font-weight:500;color:var(--accent)}
.account{top:44px;font-size:12px;font-weight:500;color:#444}
.search{left:663px;top:86px;width:128px;height:21px;border:1px solid #bbb;border-radius:11px;background:#fff;font-size:10px;color:#aaa;padding:4px 0 0 21px}
.search svg{position:absolute;left:7px;top:5px}
.mainnav{left:104px;top:124px;width:680px;display:flex;justify-content:space-between;align-items:baseline;font-family:"Arimo",sans-serif;font-size:13px;color:#555}
.mainnav .home{font-size:21px;font-weight:700;letter-spacing:-1px;color:#444}
.artist-name{left:110px;top:179px;font-size:18px;font-weight:500;color:#555}
.tabs{left:104px;top:212px;width:667px;height:28px;background:linear-gradient(#fafafa,#ececec);border:1px solid #ccc;border-radius:8px;box-shadow:inset 2px 2px 3px rgba(0,0,0,.12);font-size:14px;color:#555}
.tab{position:absolute;top:0;height:26px;line-height:26px;border-right:1px solid #ccc;text-align:center}
.tab.on{background:var(--accent);color:#555;border:1px solid #a9ad1c;border-radius:2px}
.panel{left:103px;top:253px;width:668px;height:444px;background:var(--panel);border:1px solid var(--line);box-shadow:0 14px 18px -10px rgba(0,0,0,.35)}
.avatar{left:122px;top:278px;width:102px;height:75px;background:linear-gradient(#7a7f6c,#b9b9b0 60%,#dcdcd6)}
.roles{left:122px;top:372px;font-size:11.5px;line-height:19px;color:#444}
.dots{left:122px;top:437px;width:100px;border-top:1px dotted #777}
.facts-title{left:122px;top:460px;font-size:16px;font-weight:700;color:var(--accent-text);letter-spacing:-1px}
.facts{left:123px;top:489px;font-size:11px;line-height:20.5px;color:#444}
.artwork{left:241px;top:278px;width:512px;height:297px;background:linear-gradient(#3b3a34 0%,#c9a46a 30%,#c8b98c 55%,#6c9bb8 68%,#7b7161 85%,#4a4235);border:1px solid #333}
.caption{left:241px;top:579px;width:512px;text-align:center;font-size:10px;color:#333}
.thumb{top:614px;width:60px;height:60px}
.ctrl{top:632px}
.social{left:695px;top:711px;display:flex;gap:3px}
.social span{width:16px;height:16px;background:#3a3a3a;border-radius:2px}
.h2{font-size:18px;font-weight:700;letter-spacing:-1px;color:#3a3a3a}
.actions-title{left:121px;top:742px}
.actions{top:776px;font-size:13.5px;line-height:25.7px;color:#333}
.info-title{left:448px;top:737px;display:flex;align-items:center;gap:6px}
.info{left:447px;top:764px;width:324px;height:102px;background:var(--box);border:1px solid #e3e3e3;padding:8px 20px;font-size:11.5px;line-height:19px;color:#444}
.info em{font-style:normal;color:var(--accent-text)}
.lower{left:104px;top:896px;width:667px;height:156px;background:var(--box);border:1px solid #ddd}
.news-title{left:121px;top:903px}
.news{left:121px;top:934px;font-size:11.5px;line-height:19px;color:#333}
.statement-title{left:451px;top:903px}
.statement{left:452px;top:931px;width:305px;font-size:11.5px;line-height:19px;color:#444}
.footnav{left:0;top:1085px;width:874px;display:flex;justify-content:center;gap:28px;font-family:"Arimo",sans-serif;font-size:9.5px;font-weight:700;letter-spacing:-.5px;color:#444}
.copyright{left:0;top:1115px;width:874px;text-align:center;font-family:"Arimo",sans-serif;font-size:8.5px;color:#333}
.feedback{left:0;top:431px;width:33px;height:123px;background:#3a3a3a;border:1px solid #777;border-left:none;color:#fff;font-size:14px;font-weight:700;writing-mode:vertical-rl;display:flex;align-items:center;justify-content:center}
</style>
</head>
<body>
<div class="abs citybar">
  <span>Chicago</span><span class="sep">|</span><span>Los Angeles</span><span class="sep">|</span><span>Miami</span><span class="sep">|</span><span>New York</span><span class="sep">|</span><span>San Francisco</span><span class="sep">|</span><span>Santa Fe I Amsterdam</span><span class="sep">|</span><span>Berlin</span><span class="sep">|</span><span>Brussels</span><span class="sep">|</span><span>London</span><span class="sep">|</span><span>Paris</span><span class="sep">|</span><span>China</span><span class="sep">|</span><span>India</span><span class="sep">|</span><span>Worldwide</span>
</div>

<div class="abs brand"><span class="brand-name">CanvoMira</span><span class="brand-sub">Worldwide</span></div>
<div class="abs account" style="left:600px">Register Free</div>
<div class="abs account" style="left:698px">Sign in</div>
<div class="abs account" style="left:772px">FAQ</div>
<div class="abs search"><svg width="9" height="9" viewBox="0 0 9 9"><circle cx="3.6" cy="3.6" r="2.8" fill="none" stroke="#aaa" stroke-width="1.2"/><line x1="5.6" y1="5.6" x2="8.4" y2="8.4" stroke="#aaa" stroke-width="1.4"/></svg>search the ew site</div>

<nav class="abs mainnav">
  <span class="home">HOME</span><span>MAGAZINE</span><span>CALENDAR</span><span>GALLERIES</span><span>ART</span><span>SHOP</span><span>ARTISTS</span><span>COMMUNITY</span><span>ADD</span>
</nav>

<h1 class="abs artist-name">Orin Haskel</h1>

<div class="abs tabs">
  <div class="tab on" style="left:85px;width:60px">Profile</div>
  <div class="tab" style="left:148px;width:92px">Artworks</div>
  <div class="tab" style="left:240px;width:86px">For sale</div>
  <div class="tab" style="left:326px;width:88px">Network</div>
  <div class="tab" style="left:414px;width:94px">Reviews</div>
  <div class="tab" style="left:508px;width:96px">Comments</div>
</div>

<div class="abs panel"></div>
<div class="abs avatar" role="img" aria-label="Profile photo of the artist seated on a park chair"></div>
<div class="abs roles">Artist<br>Writer<br>Artlover</div>
<div class="abs dots"></div>
<div class="abs facts-title">QUICK FACTS</div>
<div class="abs facts">Birthplace:&nbsp; Paris<br>Birth Year:&nbsp; 1974<br>Lives In:&nbsp; Paris<br>Works In:&nbsp; Paris</div>
<div class="abs artwork" role="img" aria-label="Featured artwork: photograph of a painted wall beside railway tracks"></div>
<div class="abs caption">Rail Study Lakeside 11 (from Trackside Passage Seri..., 2010</div>

<svg class="abs ctrl" style="left:128px" width="20" height="20" viewBox="0 0 20 20"><circle cx="10" cy="10" r="9" fill="#e3e3e3"/><path d="M10 6v8L5 10zM15 6v8l-5-4z" fill="#555"/></svg>
<div class="abs thumb" style="left:160px;background:linear-gradient(#6f8fae,#3a2e28)" role="img" aria-label="Portrait photograph thumbnail"></div>
<div class="abs thumb" style="left:228px;background:linear-gradient(#b85a4a,#2a2422)" role="img" aria-label="Portrait photograph thumbnail"></div>
<div class="abs thumb" style="left:298px;background:linear-gradient(#c9c2b8,#2b2422)" role="img" aria-label="Portrait photograph thumbnail"></div>
<div class="abs thumb" style="left:368px;background:linear-gradient(#d07c6c,#4a2f4f)" role="img" aria-label="Portrait photograph thumbnail"></div>
<div class="abs thumb" style="left:438px;background:linear-gradient(#d7d3cc,#5a4c40)" role="img" aria-label="Portrait photograph thumbnail"></div>
<div class="abs thumb" style="left:506px;background:linear-gradient(#c5b58f,#3e3530)" role="img" aria-label="Portrait photograph thumbnail"></div>
<div class="abs thumb" style="left:573px;background:linear-gradient(#6b6a52,#2a2724)" role="img" aria-label="Portrait photograph thumbnail"></div>
<div class="abs thumb" style="left:638px;background:linear-gradient(#8c857a,#2a2522)" role="img" aria-label="Portrait photograph thumbnail"></div>
<svg class="abs ctrl" style="left:703px;top:628px" width="28" height="28" viewBox="0 0 28 28"><circle cx="14" cy="14" r="13" fill="#e3e3e3"/><path d="M10 8v12l10-6z" fill="#444"/></svg>
<svg class="abs ctrl" style="left:738px" width="20" height="20" viewBox="0 0 20 20"><circle cx="10" cy="10" r="9" fill="#e3e3e3"/><path d="M5 6v8l5-4zM10 6v8l5-4z" fill="#555"/></svg>

<div class="abs social"><span></span><span></span><span></span><span></span></div>

<h2 class="abs h2 actions-title">Actions</h2>
<div class="abs actions" style="left:122px">Add to mylist<br>View large slideshow<br>Email this artist<br>Report abuse</div>
<div class="abs actions" style="left:309px">Contact us for help<br>Pinbit this<br>Stash it!</div>

<div class="abs info-title"><svg width="15" height="13" viewBox="0 0 15 13"><path d="M7.5 0L15 13H0z" fill="#f0a91c"/><rect x="6.8" y="4" width="1.4" height="5" fill="#fff"/><rect x="6.8" y="10" width="1.4" height="1.4" fill="#fff"/></svg><h2 class="h2">Info</h2></div>
<div class="abs info">Lorem ipsum dolor sit amet,<br>consectetur adipisicing elit, sed do eiusmod tempor incididunt ut labore et dolore magna aliqua. voluptate velit esse cillum dolore eu <em>fugiat nulla pariatur</em></div>

<div class="abs lower"></div>
<h2 class="abs h2 news-title">News &amp; Buzz</h2>
<div class="abs news">Watchlist Artist: Dela Quorn<br>Watchlist Artist: Sela Ravik<br>Tavo Renn:On Our Worldwide Watchlist</div>
<h2 class="abs h2 statement-title">Statement</h2>
<p class="abs statement">Orin Haskel lives and works in and around Paris. His photography has been shown in all kinds of small galleries, clubs, and alternative arts spaces.He is particularly interested in creating a documentation of people in ordinary, everyday activities, looking for the moments of beauty or magic in the quotidien.</p>

<nav class="abs footnav"><span>CONTACT</span><span>ABOUT</span><span>ADVERTISE</span><span>TERMS</span><span>JOIN THE TEAM</span><span>FAQ</span></nav>
<div class="abs copyright">Copyright © 2006-2012 by CanvoMira, Inc. All images and content remain the © of their rightful owners.</div>

<div class="abs feedback">Feedback</div>
</body>
</html>
```